DL size flyer design for renovations and extensions construction company

We are looking for a flyer design for a construction company specialising in renovations, extensions, and minor building works. The aim is for anyone needing any home construction works to pick up the phone and call us. The flyers will be delivered primarily to letterboxes of homes. We want the flyers to stick out from all the other things people get in the mail by any means possible.

Target Market(s)

The audience we target is residential home owners and are looking to deliver these letters to home letterboxes.

Industry/Entity Type

Residential Construction

Font styles to use
Sans Serif

Colors
000000
ffffff

Requirements
Must have
• 1 - Places for 4 photos with descriptions reading: (1) Bathroom Renovations (4) Kitchen Renovations (3) Home Extensions (4) Outdoor works and landscaping. This may be on the reverse side of the DL flyer.
• 2 - Fonts to be used are (1) Brandon Grotesque (All caps) for main heading, (2) Montserrat SemiBold (All caps) for Headings, (3) Lato for text.
• 3 - Copy of the finished document in PDF and indesign formats.
• 4 - Placeholders for copy (look at the pelvaridge.com website for now)
Nice to have
• A modern looking design.
Should not have
• Not all photos attached are necessarily required. Up to you to use your creativity to decide on the best combination.

```html
<!DOCTYPE html>
<html lang="en">
<head>
<meta charset="utf-8">
<title>Harlowe Build – Build. Renovate. Extend.</title>
<link rel="stylesheet" href="https://fonts.googleapis.com/css2?family=Josefin+Sans:wght@300;700&family=Lato:wght@400;700&family=Montserrat:wght@400;600&display=swap">
<style>
  :root {
    --green: #4db38e;
    --ink: #1f1f1f;
    --paper: #ffffff;
    --backdrop: #dfe2e6;
    --panel-w: 280px;
    --panel-h: 590px;
  }
  * { box-sizing: border-box; margin: 0; padding: 0; }
  html, body { width: 1200px; height: 1116px; overflow: hidden; }
  body {
    background: var(--backdrop);
    font-family: "Lato", sans-serif;
    color: var(--ink);
    position: relative;
  }
  .spread, .cover {
    position: absolute;
    top: 263px;
    height: var(--panel-h);
    background: var(--paper);
    box-shadow: 0 6px 24px rgba(0,0,0,.12);
  }
  .spread { left: 30px; width: calc(var(--panel-w) * 3); display: flex; }
  .cover { left: 890px; width: var(--panel-w); display: flex; flex-direction: column; }
  .panel { width: var(--panel-w); height: 100%; position: relative; overflow: hidden; }
  .panel + .panel { border-left: 1px solid #e4e4e4; }

  /* Services panel */
  .panel-services { background: linear-gradient(180deg, #d9d9d9 0%, #f3f3f3 30%, #ffffff 100%); }
  .services-title {
    font-family: "Montserrat", sans-serif; font-weight: 600; text-transform: uppercase;
    font-size: 24px; letter-spacing: .5px; margin: 150px 0 10px 22px;
  }
  .services-photo { height: 160px; margin-left: 22px; background: linear-gradient(160deg, #8a9aa8 0%, #6c7a5f 45%, #b9aa88 100%); }
  .services-box {
    background: var(--green); color: var(--paper);
    margin-left: 22px; padding: 18px 16px 22px;
    font-size: 10px; line-height: 1.5;
  }
  .services-box p + p { margin-top: 8px; }
  .services-box strong { font-weight: 700; }

  /* Service sections */
  .service { height: 50%; position: relative; display: flex; flex-direction: column; }
  .service-photo { height: 160px; flex: none; position: relative; }
  .service-photo .fill { position: absolute; inset: 0; }
  .service-title {
    position: absolute; left: 14px; bottom: 14px;
    font-family: "Montserrat", sans-serif; font-weight: 400; text-transform: uppercase;
    color: var(--paper); font-size: 14px; line-height: 1.15; letter-spacing: .3px;
  }
  .service-title b { font-weight: 600; }
  .accent-bar { position: absolute; left: 0; right: 40px; bottom: 0; height: 6px; background: var(--green); }
  .service-copy { padding: 12px 16px; font-size: 8.6px; line-height: 1.5; }
  .service-copy p + p { margin-top: 7px; }

  .fill-bath { background: linear-gradient(150deg, #f4f4f2 0%, #d8d6d2 50%, #8c8a86 100%); }
  .fill-kitchen { background: linear-gradient(160deg, #f7f7f6 0%, #dedfdc 55%, #8a6a4c 100%); }
  .fill-extension { background: linear-gradient(150deg, #e8e6e2 0%, #9a8e7c 50%, #5d4030 100%); }
  .fill-outdoor { background: linear-gradient(160deg, #6b4a32 0%, #48593a 55%, #2f3b28 100%); }

  /* Cover */
  .brand {
    height: 70px; flex: none; display: flex; align-items: center; justify-content: flex-end; gap: 8px;
    padding-right: 20px;
    font-family: "Lato", sans-serif; font-weight: 700; font-size: 16px; letter-spacing: 1px;
    color: var(--ink); text-transform: uppercase; white-space: nowrap;
  }
  .brand .mark { width: 12px; height: 12px; background: var(--green); }
  .cover-photo { height: 345px; flex: none; margin-left: 16px; background: linear-gradient(165deg, #f2f1ee 0%, #c9c4bb 45%, #8a5a34 75%, #5c3a22 100%); }
  .cover-bar { height: 6px; flex: none; background: var(--green); margin-left: 16px; margin-right: 40px; }
  .tagline {
    margin-top: 24px; padding-right: 20px; text-align: right;
    font-family: "Josefin Sans", sans-serif; text-transform: uppercase;
    font-size: 30px; line-height: 1.15;
  }
  .tagline .light { font-weight: 300; color: var(--ink); display: block; }
  .tagline .strong { font-weight: 700; color: var(--green); display: block; }
</style>
</head>
<body>
  <main class="spread">
    <section class="panel panel-services">
      <h1 class="services-title">Services</h1>
      <div class="services-photo" role="img" aria-label="Photo of a rear house extension under construction beside an older home"></div>
      <div class="services-box">
        <p>Our building works span as far as your ambitions.</p>
        <p><strong>From custom kitchens and bathrooms, to bespoke joinery for renovating your study, bedrooms, laundry and other living areas.</strong></p>
        <p>We can alter or extend the layout of your home, or create an escape from the daily grind with landscape gardening and other outdoor works.</p>
      </div>
    </section>

    <section class="panel">
      <article class="service">
        <div class="service-photo">
          <div class="fill fill-bath" role="img" aria-label="Photo of a bright white bathroom with freestanding bath and glass shower"></div>
          <h2 class="service-title">Bathroom <b>Renovations</b></h2>
          <span class="accent-bar"></span>
        </div>
        <div class="service-copy">
          <p>We create custom bathroom renovations of various shapes and sizes to suit a variety of family needs.</p>
          <p>When considering a bathroom design you will need to take into account a variety of factors including the size of the existing space and whether it can be enlarged, how many people in your family will use the bathroom, if your family size is likely to increase, where the bathroom is located in the home as well as many other considerations.</p>
        </div>
      </article>
      <article class="service">
        <div class="service-photo">
          <div class="fill fill-kitchen" role="img" aria-label="Photo of a white kitchen with island bench and timber stools"></div>
          <h2 class="service-title">Kitchen <b>Renovations</b></h2>
          <span class="accent-bar"></span>
        </div>
        <div class="service-copy">
          <p>Today's kitchens go further than places to just make a meal – they are the open-plan hub for the modern home.</p>
          <p>Each kitchen will need to work in with each family's unique needs. That's why it's important to work in with an experienced designer and builder on your renovation project.</p>
        </div>
      </article>
    </section>

    <section class="panel">
      <article class="service">
        <div class="service-photo">
          <div class="fill fill-extension" role="img" aria-label="Photo of an open-plan kitchen and dining extension with pendant lights"></div>
          <h2 class="service-title">Structural Alterations<br>+ Extensions</h2>
          <span class="accent-bar"></span>
        </div>
        <div class="service-copy">
          <p>Structural alterations or extensions are an essential consideration when things simply won't fit or you want to make your home bigger or better.</p>
          <p>Harlowe Build are licenced builders experienced at delivering structural alterations or home extensions, and we are always guided by our qualified engineers.</p>
        </div>
      </article>
      <article class="service">
        <div class="service-photo">
          <div class="fill fill-outdoor" role="img" aria-label="Photo of a timber pergola over a garden deck"></div>
          <h2 class="service-title">Outdoor Works<br>+ <b>Landscaping</b></h2>
          <span class="accent-bar"></span>
        </div>
        <div class="service-copy">
          <p>We design and build decks, pergolas, paving and gardens that turn your backyard into an easy space for family living all year round.</p>
        </div>
      </article>
    </section>
  </main>

  <aside class="cover">
    <div class="brand"><span>Harlowe Build</span><span class="mark"></span></div>
    <div class="cover-photo" role="img" aria-label="Photo of a modern open-plan kitchen with timber floors and glass doors"></div>
    <div class="cover-bar"></div>
    <p class="tagline">
      <span class="light">Build.</span>
      <span class="strong">Renovate.</span>
      <span class="light">Extend.</span>
    </p>
  </aside>
</body>
</html>
```